Stay Bright Always bookcover

A graphic for quotes and front and back book cover

The title for this book is; The Pocket Silver saying Volume By Rona T. Vasquell With Luke and Miriam Holcroft I like the black cover... with colored title, purple, mint colors are good.

I would like to change this..... The title is now Walking Past Rain. I would like to use orange with maybe some bamboo

Target Market(s)

female 25-75

Industry/Entity Type

Motivation

Font styles to use
Decorative
Script

Requirements
Must have
• Jewel Colors/ Let's use hydrangea flowers w a dark background- realistic looking if possible...

Book title....... "Stay Bright Always: Words To Uplift"
Nice to have
• A little bit of sparkle, maybe gold

```html
<!DOCTYPE html>
<html lang="en">
<head>
<meta charset="utf-8">
<title>Walking Past Rain – Book Cover</title>
<link href="https://fonts.googleapis.com/css2?family=Great+Vibes&family=Kaushan+Script&family=Montserrat:wght@300;700&display=swap" rel="stylesheet">
<style>
  :root {
    --backdrop: #808084;
    --paper: #ffffff;
    --sun-orange: #f26722;
    --bamboo-green: #2a8c3c;
    --bamboo-light: #4fae5c;
  }
  * { margin: 0; padding: 0; box-sizing: border-box; }
  html, body {
    width: 1200px;
    height: 1200px;
    overflow: hidden;
    background: var(--backdrop);
  }
  .canvas {
    position: relative;
    width: 1200px;
    height: 1200px;
    background: var(--backdrop);
  }
  .book-cover {
    position: absolute;
    left: 360px;
    top: 240px;
    width: 480px;
    height: 720px;
    background: var(--paper);
    overflow: hidden;
  }
  .sun-disc {
    position: absolute;
    left: 0;
    top: 0;
    width: 480px;
    height: 720px;
  }
  .bamboo-art {
    position: absolute;
    left: 342px;
    top: 321px;
    width: 138px;
    height: 399px;
    background: linear-gradient(160deg, rgba(79,174,92,0.55) 0%, var(--bamboo-green) 100%);
    clip-path: polygon(8% 0, 40% 0, 100% 20%, 100% 100%, 45% 100%, 0 35%);
  }
  .title {
    color: var(--paper);
    position: absolute;
    white-space: nowrap;
    line-height: 1;
  }
  .title-walking {
    left: 14px;
    top: 118px;
    font-family: "Great Vibes", cursive;
    font-size: 118px;
  }
  .title-past {
    left: 208px;
    top: 262px;
    font-family: "Montserrat", sans-serif;
    font-weight: 300;
    font-size: 50px;
  }
  .title-rain {
    left: 92px;
    top: 316px;
    font-family: "Kaushan Script", cursive;
    font-size: 96px;
    transform: rotate(-6deg);
    transform-origin: left center;
  }
  .authors {
    position: absolute;
    left: 33px;
    top: 628px;
    font-family: "Montserrat", sans-serif;
    font-weight: 700;
    font-size: 20px;
    line-height: 26px;
    color: var(--sun-orange);
  }
  .authors .joiner { color: var(--bamboo-green); }
</style>
</head>
<body>
  <main class="canvas">
    <section class="book-cover">
      <svg class="sun-disc" viewBox="0 0 480 720" aria-hidden="true">
        <circle cx="184" cy="290" r="259" fill="var(--sun-orange)"/>
      </svg>

      <h1 class="book-title">
        <span class="title title-walking">Walking</span>
        <span class="title title-past">Past</span>
        <span class="title title-rain">Rain</span>
      </h1>

      <div class="bamboo-art" role="img" aria-label="Illustration of green bamboo stalks with leaves"></div>

      <p class="authors">
        Rona T. Vasquell With Luke<br>
        <span class="joiner">and</span> Miriam Holcroft
      </p>
    </section>
  </main>
</body>
</html>
```